Calloway Pizza - Takeout Menu Design

We are looking for a takeout menu design.
We are looking for a( 5" x 8.5" DOUBLE SIDED) flyer with our available pizza flavors
Must be easy to ready and not "busy"

Must include our logo (attached)
website: www.callowaypizza.example
address:
Tern Ridge Plaza
314, 418 9 Avenue SW
and the following details:
Visit our website for our complete appetizer, pasta, salad and catering menu.

Winner of this contest will also be offered to create a few print designs via artpoolhub.

Please do not hesitate to ask any questions.

Target Market(s)

Business / Office clientele

Industry/Entity Type

Pizza place / specializing in corporate orders

Requirements
Must have
• Easy to read
Should not have
• Can not be busy or cluttered

```html
<!DOCTYPE html>
<html lang="en">
<head>
<meta charset="utf-8">
<title>Calloway Pizza – Take-Out Menu</title>
<link rel="stylesheet" href="https://fonts.googleapis.com/css2?family=Montserrat:wght@300;400;500;700&family=Poppins:wght@600;700&display=swap">
<style>
  :root {
    --board: #58595b;
    --ink: #231f20;
    --red: #b3262d;
    --red-deep: #861a1f;
    --rule: #c9343a;
    --paper: #ffffff;
    --gold: #f5d31c;
    --crust-light: #f4d08a;
    --crust-dark: #b8602a;
  }
  * { box-sizing: border-box; margin: 0; padding: 0; }
  html, body { width: 1200px; height: 1036px; overflow: hidden; background: var(--board); }
  body { position: relative; font-family: "Montserrat", sans-serif; color: var(--ink); }

  .brand-mark { position: absolute; left: 260px; top: 38px; width: 678px; height: 92px; }
  .brand-mark text { font-family: "Montserrat", sans-serif; font-weight: 300; fill: var(--ink); }

  .flyer {
    position: absolute; top: 190px; width: 448px; height: 761px;
    background: var(--paper); overflow: hidden;
    box-shadow: 0 10px 24px rgba(0,0,0,.35);
  }
  .flyer--front { left: 143px; }
  .flyer--back { left: 605px; }

  .side-band {
    position: absolute; left: 0; top: 0; width: 109px; height: 714px;
    background: linear-gradient(90deg, var(--red-deep), var(--red));
  }
  .side-band .side-name { position: absolute; left: 0; top: 0; width: 109px; height: 714px; }
  .side-band .side-name text { font-family: "Montserrat", sans-serif; font-weight: 300; fill: var(--paper); }

  .pizza-photo {
    position: absolute; left: -124px; top: 18px; width: 244px; height: 244px; border-radius: 50%;
    background: radial-gradient(circle at 55% 50%, var(--crust-light) 0%, #e7a85a 55%, var(--crust-dark) 88%, #8d4a1e 100%);
    box-shadow: 4px 6px 12px rgba(0,0,0,.35);
  }

  .promo-band {
    position: absolute; left: 109px; top: 0; width: 339px; height: 87px;
    background: linear-gradient(100deg, #3a2a20 0%, #6b4a2c 45%, #3b2a1e 100%);
  }
  .promo-text {
    position: absolute; left: 138px; top: 16px; width: 300px;
    font-family: "Poppins", sans-serif; font-weight: 600; font-size: 14.6px; line-height: 17.4px;
    color: var(--paper);
  }

  .menu { position: absolute; left: 130px; width: 295px; }
  .menu-head {
    display: grid; grid-template-columns: 1fr 48px 35px; align-items: end;
    font-family: "Poppins", sans-serif; font-weight: 700; font-size: 14.3px; line-height: 16px;
  }
  .menu-head span { display: inline-block; border-bottom: 3px solid var(--red); padding-bottom: 1px; }
  .menu-head .size { text-align: center; }

  .classic-list { list-style: none; margin-top: 8px; }
  .classic-list li {
    display: grid; grid-template-columns: 1fr 48px 35px; align-items: center;
    height: 22.4px; padding-left: 8px; font-size: 12.8px; border-bottom: 1px solid var(--rule);
  }
  .classic-list li:last-child { border-bottom: none; }
  .price { font-size: 11.4px; }

  .specialty-list { list-style: none; margin-top: 9px; }
  .specialty-list li {
    display: grid; grid-template-columns: 1fr 48px 35px; align-items: start;
    padding: 1px 0 3px 8px; border-bottom: 1px solid var(--rule);
  }
  .specialty-list--roomy li { padding: 2px 0 4px 8px; }
  .specialty-list li:last-child { border-bottom: none; }
  .item-name { display: block; font-weight: 700; color: var(--red); font-size: 12.8px; line-height: 12.6px; }
  .item-desc { display: block; font-size: 9.9px; line-height: 10.4px; }
  .specialty-list .price { padding-top: 1px; }

  .feature-band {
    position: absolute; left: 109px; top: 646px; width: 339px; height: 54px;
    background: linear-gradient(90deg, var(--red-deep), var(--red));
    color: var(--paper); padding: 3px 24px 0 29px;
    display: grid; grid-template-columns: 1fr 48px 35px; align-items: end;
  }
  .feature-band .item-name { color: var(--gold); line-height: 14px; }
  .feature-band .item-desc { font-size: 9.8px; line-height: 12px; }
  .feature-band .price { color: var(--gold); font-weight: 700; line-height: 12.4px; padding-bottom: 3px; }

  .footer-band {
    position: absolute; left: 0; top: 714px; width: 448px; height: 19px;
    background: #000; color: var(--paper); font-size: 10.3px; font-weight: 500;
    display: flex; align-items: center; justify-content: center;
  }
  .contact-row {
    position: absolute; left: 22px; right: 22px; top: 735px;
    display: flex; justify-content: space-between; font-size: 9.6px; color: var(--red);
  }
  .contact-row span { display: inline-flex; align-items: center; gap: 5px; }
  .contact-row svg { width: 9px; height: 10px; }
</style>
</head>
<body>

<svg class="brand-mark" viewBox="0 0 678 92" aria-label="Calloway Pizza">
  <text x="0" y="88" font-size="118" textLength="678" lengthAdjust="spacingAndGlyphs">CALLOWAYPIZZA</text>
</svg>

<section class="flyer flyer--front">
  <div class="side-band">
    <div class="pizza-photo" role="img" aria-label="Photo of a pepperoni pizza"></div>
    <svg class="side-name" viewBox="0 0 109 714" aria-label="Calloway Pizza">
      <text transform="translate(78 698) rotate(-90)" font-size="74" textLength="419" lengthAdjust="spacingAndGlyphs">CALLOWAYPIZZA</text>
    </svg>
  </div>
  <div class="promo-band" role="img" aria-label="Close-up photo of melted cheese on pizza"></div>
  <p class="promo-text">All of our pizzas are prepared fresh everyday using only the finest mozzarella blend and ingredients.</p>

  <div class="menu" style="top:94px">
    <div class="menu-head"><div><span>CLASSIC TAKE-OUT PIZZA</span></div><div class="size"><span>8"</span></div><div class="size"><span>13"</span></div></div>
    <ul class="classic-list">
      <li>Pepperoni &amp; Mushroom<span class="price">$12.99</span><span class="price">$30.95</span></li>
      <li>Pepperoni<span class="price">$11.99</span><span class="price">$29.95</span></li>
      <li>Hawaiian<span class="price">$12.99</span><span class="price">$30.95</span></li>
      <li>Beef &amp; Mushroom<span class="price">$13.49</span><span class="price">$32.95</span></li>
      <li>Pepperoni &amp; Ham<span class="price">$12.99</span><span class="price">$30.95</span></li>
      <li>Ham &amp; Mushroom<span class="price">$12.99</span><span class="price">$30.95</span></li>
      <li>Beef &amp; Onion<span class="price">$13.49</span><span class="price">$32.95</span></li>
      <li>Cheese<span class="price">$11.99</span><span class="price">$29.95</span></li>
    </ul>
  </div>

  <div class="menu" style="top:305px">
    <div class="menu-head"><div><span>SPECIALTY TAKE-OUT PIZZA</span></div><div class="size"><span>8"</span></div><div class="size"><span>13"</span></div></div>
    <ul class="specialty-list">
      <li><div><span class="item-name">All Meat</span><span class="item-desc">Pepperoni, Beef &amp; Smoked<br>Ham &amp; Bacon</span></div><span class="price">$14.99</span><span class="price">$35.95</span></li>
      <li><div><span class="item-name">Double Pepperoni</span><span class="item-desc">Loads of Pepperoni</span></div><span class="price">$13.49</span><span class="price">$32.95</span></li>
      <li><div><span class="item-name">Hot Honey Pepperoni</span><span class="item-desc">Double Pepperoni and<br>drizzled with Hot Honey</span></div><span class="price">$14.49</span><span class="price">$34.95</span></li>
      <li><div><span class="item-name">Hawaiian Heat</span><span class="item-desc">Smoked Ham,<br>Pineapple and Banana Peppers</span></div><span class="price">$13.49</span><span class="price">$32.95</span></li>
      <li><div><span class="item-name">Four Cheese</span><span class="item-desc">Mozzarella, Feta, Romano<br>and Cheddar Cheese</span></div><span class="price">$13.49</span><span class="price">$32.95</span></li>
      <li><div><span class="item-name">Montreal</span><span class="item-desc">Pepperoni &amp;<br>Double Smoked Bacon</span></div><span class="price">$13.49</span><span class="price">$32.95</span></li>
      <li><div><span class="item-name">Montreal Heat</span><span class="item-desc">Pepperoni, Double Smoked<br>Bacon &amp; Banana Peppers</span></div><span class="price">$13.99</span><span class="price">$33.95</span></li>
      <li><div><span class="item-name">Supreme</span><span class="item-desc">Pepperoni, Mushrooms &amp;<br>Green Peppers</span></div><span class="price">$13.49</span><span class="price">$32.95</span></li>
      <li><div><span class="item-name">Canadian</span><span class="item-desc">Pepperoni, Mushrooms &amp; Ham</span></div><span class="price">$13.49</span><span class="price">$32.95</span></li>
      <li><div><span class="item-name">BBQ Chicken</span><span class="item-desc">Chicken Breast,<br>Hickory BBQ Sauce &amp; Red Onions.</span></div><span class="price">$13.99</span><span class="price">$33.95</span></li>
    </ul>
  </div>

  <div class="footer-band">Visit our website for our complete appetizer, pasta, salad and catering menu</div>
  <div class="contact-row">
    <span><svg viewBox="0 0 10 12"><path d="M5 0a4 4 0 0 0-4 4c0 3 4 8 4 8s4-5 4-8a4 4 0 0 0-4-4zm0 5.6A1.6 1.6 0 1 1 5 2.4a1.6 1.6 0 0 1 0 3.2z" fill="#231f20"/></svg>Tern Ridge Plaza 314, 418 9 Avenue SW</span>
    <span><svg viewBox="0 0 12 12"><g fill="none" stroke="#231f20" stroke-width="1.1"><circle cx="6" cy="6" r="5"/><ellipse cx="6" cy="6" rx="2.2" ry="5"/><path d="M1 6h10M2 3.3h8M2 8.7h8"/></g></svg>www.callowaypizza.example</span>
  </div>
</section>

<section class="flyer flyer--back">
  <div class="side-band">
    <div class="pizza-photo" role="img" aria-label="Photo of a pepperoni pizza"></div>
    <svg class="side-name" viewBox="0 0 109 714" aria-label="Calloway Pizza">
      <text transform="translate(78 698) rotate(-90)" font-size="74" textLength="419" lengthAdjust="spacingAndGlyphs">CALLOWAYPIZZA</text>
    </svg>
  </div>

  <div class="menu" style="top:20px">
    <div class="menu-head"><div><span>SPECIALTY TAKE-OUT PIZZA</span></div><div class="size"><span>8"</span></div><div class="size"><span>13"</span></div></div>
    <ul class="specialty-list specialty-list--roomy">
      <li><div><span class="item-name">BBQ Chicken Plus</span><span class="item-desc">Chicken Breast, Hickory BBQ Sauce,<br>Red Onions &amp; Cilantro</span></div><span class="price">$14.79</span><span class="price">$34.95</span></li>
      <li><div><span class="item-name">Spicy BBQ Chicken</span><span class="item-desc">Chicken Breast, Hickory BBQ Sauce,<br>Red Onions &amp; Banana Peppers</span></div><span class="price">$14.49</span><span class="price">$35.95</span></li>
      <li><div><span class="item-name">Sweet Chili Chicken</span><span class="item-desc">Chicken Breast, Pineapple,<br>Red Onions &amp; Sweet Chili Sauce</span></div><span class="price">$14.49</span><span class="price">$35.95</span></li>
      <li><div><span class="item-name">Chicken Club</span><span class="item-desc">Chicken Breast, Double Smoked Bacon,<br>Red Onions and Tomatoes</span></div><span class="price">$14.79</span><span class="price">$35.95</span></li>
      <li><div><span class="item-name">Athenean</span><span class="item-desc">Chicken Breast, Spinach,<br>Feta Cheese and Tomato</span></div><span class="price">$14.49</span><span class="price">$34.95</span></li>
      <li><div><span class="item-name">Greek Supreme</span><span class="item-desc">Chicken Breast, Feta Cheese, Tomato,<br>Green Pepper, Red Onions &amp; Black Olives</span></div><span class="price">$14.99</span><span class="price">$35.95</span></li>
      <li><div><span class="item-name">Mediterranean Chicken</span><span class="item-desc">Seasoned Chicken Breast, Tomatoes,<br>Red Onions and Feta Cheese</span></div><span class="price">$14.79</span><span class="price">$35.95</span></li>
      <li><div><span class="item-name">Original Spinach</span><span class="item-desc">Spinach &amp; Feta Cheese</span></div><span class="price">$13.49</span><span class="price">$32.95</span></li>
      <li><div><span class="item-name">Zeus</span><span class="item-desc">Spinach, Feta Cheese<br>and Tomatoes</span></div><span class="price">$13.95</span><span class="price">$33.95</span></li>
      <li><div><span class="item-name">Greek</span><span class="item-desc">Feta Cheese, Tomato, Green Peppers,<br>Red Onions and Black Olives</span></div><span class="price">$13.99</span><span class="price">$33.95</span></li>
      <li><div><span class="item-name">Vegetarian</span><span class="item-desc">Mushrooms, Tomatoes,<br>Green Peppers and Black Olives</span></div><span class="price">$13.49</span><span class="price">$32.95</span></li>
      <li><div><span class="item-name">Veggie Delight</span><span class="item-desc">Mushrooms, Tomatoes,<br>Green Peppers, Black Olives &amp; Onions</span></div><span class="price">$13.95</span><span class="price">$33.95</span></li>
      <li><div><span class="item-name">Deluxe</span><span class="item-desc">Pepperoni, Mushrooms, Ham, Tomatoes,<br>Green Peppers and Red Onions</span></div><span class="price">$14.49</span><span class="price">$34.95</span></li>
      <li><div><span class="item-name">Calloway Special</span><span class="item-desc">Pepperoni, Mushrooms, Ham,<br>Green Peppers and Black Olives</span></div><span class="price">$14.49</span><span class="price">$34.95</span></li>
      <li><div><span class="item-name">BBQ Pulled Pork</span><span class="item-desc">Pulled Pork, Red Onions,<br>Red Peppers and Cilantro.</span></div><span class="price">$14.49</span><span class="price">$35.95</span></li>
    </ul>
  </div>

  <div class="feature-band">
    <div><span class="item-name">Dill Pickle</span><span class="item-desc">Crispy Dill Pickles, Fresh Dill with<br>our cream based garlic sauce.<br>Served with our without bacon.</span></div>
    <span class="price">$14.49<br>$13.49</span>
    <span class="price">$35.95<br>$32.95</span>
  </div>

  <div class="footer-band">Visit our website for our complete appetizer, pasta, salad and catering menu</div>
  <div class="contact-row">
    <span><svg viewBox="0 0 10 12"><path d="M5 0a4 4 0 0 0-4 4c0 3 4 8 4 8s4-5 4-8a4 4 0 0 0-4-4zm0 5.6A1.6 1.6 0 1 1 5 2.4a1.6 1.6 0 0 1 0 3.2z" fill="#231f20"/></svg>Tern Ridge Plaza 314, 418 9 Avenue SW</span>
    <span><svg viewBox="0 0 12 12"><g fill="none" stroke="#231f20" stroke-width="1.1"><circle cx="6" cy="6" r="5"/><ellipse cx="6" cy="6" rx="2.2" ry="5"/><path d="M1 6h10M2 3.3h8M2 8.7h8"/></g></svg>www.callowaypizza.example</span>
  </div>
</section>

</body>
</html>
```